Kestrova Systems, an Enterprise Services Company, needs a Company Overview Sales Sheet

Our company is called Kestrova Systems and we are a leading regional systems integrator with world-class compute, storage and networking solutions and professional services for the most advanced software-defined data centers. We are currently transitioning to a Space Theme on all collateral, website designs, etc. We want to redesign our Executive Overview Sales Sheet (See attached Executive Summary Sale Sheet) with the same information but that incorporates the space theme. Should be professional and have the same blue company color scheme. Please see an example of a recent infographic we had redesigned (See Attached Kestrova QRT Infographic). Should be front and back design on full 8 1/2 x 11 and should be good for print. Trim should be 8 1/2 x 11, Bleed would be 8.75 x 11.25, Safe 8.25 x 10.75, with print quality 300dpi.

Target Market(s)

IT

Industry/Entity Type

Information Technology

Font styles to use
Serif
Sans Serif

Colors
0555a3
0392cd
3176b5
33a6d7
ffffff

Requirements
Must have
• Should be front and back design on full 8 1/2 x 11 and should be good for print. Trim should be 8 1/2 x 11, Bleed would be 8.75 x 11.25, Safe 8.25 x 10.75, with print quality 300dpi.

```html
<!DOCTYPE html>
<html lang="en">
<head>
<meta charset="utf-8">
<title>Kestrova Systems – Executive Overview</title>
<link rel="stylesheet" href="https://fonts.googleapis.com/css2?family=Bebas+Neue&family=Arimo:wght@400;700&family=Lato:wght@400;700&family=Roboto+Condensed:wght@700&display=swap">
<style>
  :root{
    --brand-deep:#0555a3;
    --brand-cyan:#0392cd;
    --brand-mid:#3176b5;
    --brand-light:#33a6d7;
    --white:#ffffff;
    --navy:#0b1a33;
    --space:#040b1c;
    --panel:rgba(20,28,45,.82);
    --stage:#2b2b2b;
  }
  *{box-sizing:border-box;margin:0;padding:0}
  html,body{width:888px;height:1200px;overflow:hidden;background:var(--stage)}
  .sheet{position:absolute;left:44px;top:84px;width:803px;height:1032px;background:var(--space);overflow:hidden;font-family:"Arimo",Arial,sans-serif;color:var(--white);hyphens:auto;-webkit-hyphens:auto}

  /* hero */
  .hero{position:absolute;left:0;top:0;width:803px;height:294px;
    background:
      radial-gradient(circle at 52% 33%, #ffffff 0, #bfe6ff 3%, #3aa0ff 10%, rgba(20,80,200,.6) 24%, rgba(5,20,60,0) 45%),
      radial-gradient(ellipse at 95% 30%, rgba(40,110,200,.5), rgba(0,0,0,0) 40%),
      linear-gradient(180deg,#06122e 0%,#0a2a66 55%,#0d3f8c 100%)}
  .brand{position:absolute;left:24px;top:38px;display:flex;align-items:center;gap:10px}
  .brand-mark{width:46px;height:46px;border-radius:8px;background:var(--white)}
  .brand-name{font-family:"Lato",sans-serif;font-weight:400;font-size:38px;line-height:46px;color:var(--brand-light);letter-spacing:-.5px}
  .brand-tag{position:absolute;left:92px;top:94px;font-family:"Lato",sans-serif;font-weight:700;font-size:13px;color:var(--white)}
  .hero-title{position:absolute;left:34px;top:164px;font-family:"Bebas Neue",sans-serif;font-weight:400;font-size:50px;line-height:1;color:var(--white);letter-spacing:.3px}
  .hero-sub{position:absolute;left:38px;top:218px;font-size:17.5px;line-height:23px;color:var(--brand-light)}
  .hero-rule{position:absolute;left:0;top:294px;width:803px;height:5px;background:var(--white)}

  /* about */
  .about{position:absolute;left:0;top:299px;width:803px;height:272px;background:linear-gradient(180deg,#1b416f 0%,#2461a0 60%,#2a6fb3 100%)}
  .section-tag{position:absolute;display:flex;align-items:center}
  .tag-icon{width:58px;height:58px;border-radius:50%;background:#e9eef3;border:3px solid #fff;position:relative;z-index:2}
  .tag-label{font-family:"Bebas Neue",sans-serif;font-weight:400;font-size:32px;line-height:36px;padding:0 22px 0 16px;margin-left:-8px;border-radius:0 6px 6px 0}
  .about .section-tag{left:36px;top:12px}
  .about .tag-label{background:var(--brand-light);color:#13335a;height:36px}
  .about-copy{position:absolute;left:32px;top:84px;width:730px;font-size:10.8px;line-height:16.4px;text-align:justify}
  .about-copy p+p{margin-top:16px}

  /* overview */
  .overview{position:absolute;left:0;top:571px;width:803px;height:392px;
    background:
      radial-gradient(ellipse at 50% 125%, #6fa6d8 0, #2c5f94 28%, #0f2a4d 44%, rgba(4,11,28,0) 60%),
      linear-gradient(180deg,#050d20 0%,#07142c 100%)}
  .overview-band{position:absolute;left:0;top:0;width:803px;height:6px;background:var(--brand-mid)}
  .overview .section-tag{left:274px;top:5px;width:200px;height:44px;background:var(--brand-deep);border-radius:0 0 8px 8px;justify-content:center;gap:8px}
  .overview .tag-icon{width:38px;height:38px;border:0;background:#fff;display:flex;align-items:center;justify-content:center}
  .overview .tag-label{font-size:34px;color:var(--brand-light);background:none;margin:0;padding:0}
  .panel{position:absolute;background:var(--panel);text-align:center}
  .panel h3{font-family:"Roboto Condensed","Arial Narrow",sans-serif;font-weight:700;font-size:14px;line-height:19px;color:var(--brand-light);text-transform:uppercase;letter-spacing:.3px;margin-bottom:6px;hyphens:manual}
  .panel p{font-size:10.8px;line-height:13.6px}
  .panel-knowledge{left:22px;top:51px;width:190px;height:174px;padding:9px 8px}
  .panel-partner{left:232px;top:96px;width:249px;height:194px;padding:13px 10px}
  .panel-partner h3{margin-bottom:12px}
  .panel-partner p{text-align:justify}
  .panel-mission{left:491px;top:51px;width:292px;height:292px;padding:9px 10px}
  .panel-mission p{text-align:justify;text-align-last:center}
  .panel-mission p+p{margin-top:12px}
  .solutions{position:absolute;left:0;top:853px;width:226px;height:104px;background:linear-gradient(180deg,#3d8fd6,#1f5fa8);border-radius:0 10px 0 0;padding:8px 10px}
  .solutions-head{display:flex;align-items:center;gap:6px}
  .solutions-icon{width:26px;height:26px;border-radius:50%;background:#fff}
  .solutions-head span{font-family:"Bebas Neue",sans-serif;font-weight:400;font-size:26px;line-height:26px;background:var(--brand-deep);padding:0 10px;border-radius:0 5px 5px 0}
  .solutions ul{list-style:none;columns:2;column-gap:6px;margin-top:8px;font-family:"Bebas Neue",sans-serif;font-size:11.5px;line-height:13.6px;color:#d7ecfb}
  .solutions li::before{content:"› "}

  /* footer */
  .footer{position:absolute;left:0;top:963px;width:803px;height:58px;background:linear-gradient(180deg,#1d63ad,#0f4e93);display:flex;align-items:center;justify-content:space-between;padding:0 26px 0 22px}
  .footer .brand{position:static;gap:6px}
  .footer .brand-mark{width:28px;height:28px;border-radius:5px}
  .footer .brand-name{font-size:24px;line-height:28px}
  .footer-contact{font-family:"Lato",sans-serif;font-weight:700;font-size:12.6px;line-height:16px;text-align:right}
  .footer-base{position:absolute;left:0;top:1021px;width:803px;height:11px;background:var(--navy)}
</style>
</head>
<body>
<main class="sheet">
  <header class="hero" role="img" aria-label="Space scene: a bright star rising over the edge of a glowing blue planet">
    <div class="brand"><span class="brand-mark"></span><span class="brand-name">Kestrova</span></div>
    <div class="brand-tag">dedicated to our clients</div>
    <h1 class="hero-title">EXECUTIVE OVERVIEW</h1>
    <p class="hero-sub">Kestrova™ world-class compute storage<br>and networking solutions</p>
  </header>
  <div class="hero-rule"></div>

  <section class="about">
    <div class="section-tag">
      <span class="tag-icon">
        <svg width="52" height="52" viewBox="0 0 52 52" aria-hidden="true"><circle cx="26" cy="20" r="8" fill="#5b6470"/><path d="M11 43c2-9 8-13 15-13s13 4 15 13z" fill="#5b6470"/></svg>
      </span>
      <span class="tag-label">ABOUT US</span>
    </div>
    <div class="about-copy">
      <p>Kestrova Systems, Inc. (Kestrova™) is a leading regional systems integrator with world-class compute, storage and networking solutions and professional services for the most advanced software-defined data centers. These competencies are tightly complimented by a full suite of data center capabilities, including private and hybrid cloud offerings, connectivity services, colocation facilities and managed services. Kestrova's converged infrastructure and software-defined data center solutions are backed by a complete range of professional services, including readiness assessments, deployment and integration, training, comprehensive project management, maintenance and financing.</p>
      <p>Kestrova's data center offerings, deployed on the most advanced technology solutions available, are hosted in carrier grade environments and include offerings for 24/7 management and monitoring for on-premises and off-premises environments. Kestrova™ holds platinumlevel designations from its manufacturer partners and consistently achieves the highest levels of client satisfaction. Among numerous accolades, Venture magazine rated Kestrova™ as No. 42 among the Fastest Growing Privately Held Companies in the United States and the No. 1 Fastest Growing in Los Angeles.</p>
    </div>
  </section>

  <section class="overview" role="img" aria-label="Night view of the Earth from orbit with city lights below a starfield">
    <div class="overview-band"></div>
    <div class="section-tag">
      <span class="tag-icon">
        <svg width="26" height="26" viewBox="0 0 26 26" aria-hidden="true"><path d="M2 13c4-6 18-6 22 0-4 6-18 6-22 0z" fill="#0b1a33"/><circle cx="13" cy="13" r="4" fill="#fff"/><circle cx="13" cy="13" r="2" fill="#0b1a33"/></svg>
      </span>
      <span class="tag-label">OVERVIEW</span>
    </div>

    <article class="panel panel-knowledge">
      <h3>Knowledge &amp; Experience</h3>
      <p>Dedicated to the highest quality service and long-term client partnerships, Kestrova™ has experienced and knowledgeable IT architects who implement and secure technology solutions that make clients more competitive.</p>
    </article>

    <article class="panel panel-partner">
      <h3>A Leading Premier Business<br>Partner of Leading Technology<br>Providers for a Decade</h3>
      <p>Kestrova™ delivers the industry's best systems by combining advanced technology services with the industry-leading products and resources of QRT, Helix, Corvane and other select partners. We focus on serving the needs of our clients in order to deliver bottom-line results and long-term business value.</p>
    </article>

    <article class="panel panel-mission">
      <h3>Our Mission</h3>
      <p>Kestrova Systems Inc. is dedicated to being the leading provider of information technology solutions in the Western United States by providing best-of-breed solutions and excellent customer service. We will continue to grow by solving complex technical and business challenges for our clients while providing opportunities for the enrichment of our Kestrova™ team.</p>
      <p>Meeting IT Challenges with Industry-Specific Solutions is something we work hard at every day. We serve a range of industries, and we've found that our clients all share an appreciation for systems that run reliably, perform beyond expectations, and contribute to the bottom line. Our technical skills, extensive multi-industry experience, and access to partners' best-of-breed technology enables us to develop reliable, high performance technology solutions that deliver industry-specific business advantages.</p>
    </article>
  </section>

  <aside class="solutions">
    <div class="solutions-head"><span class="solutions-icon"></span><span>SOLUTIONS</span></div>
    <ul>
      <li>Critical Computing</li>
      <li>Enterprise Hybrid Cloud</li>
      <li>Enterprise Storage</li>
      <li>Data Center Services</li>
      <li>Networking</li>
      <li>Analytics</li>
      <li>Professional Services</li>
    </ul>
  </aside>

  <footer class="footer">
    <div class="brand"><span class="brand-mark"></span><span class="brand-name">Kestrova</span></div>
    <p class="footer-contact">For more information, please contact us at: 4120 Meridian Court, Westlake, CA 91360,<br>877.555.0142 &nbsp;or visit www.kestrovasystems.com</p>
  </footer>
  <div class="footer-base"></div>
</main>
</body>
</html>
```